Dane Calloway Photography

Would like the Business card to have a cool logo. I’m targeting wedding/ engagement: portrait photography. My phone number on it. And my business email address.

Target Market(s)

Wedding/portrait/engagement photography.

```html
<!DOCTYPE html>
<html lang="en">
<head>
<meta charset="utf-8">
<title>Dane Calloway Photography – Business Card</title>
<link rel="stylesheet" href="https://fonts.googleapis.com/css2?family=Cinzel:wght@400;500&family=Arimo:wght@400&display=swap">
<style>
  :root {
    --backdrop: #9a9a9a;
    --card-front: #1c1c1c;
    --card-back: #000000;
    --gold: #c9a85c;
    --white: #ffffff;
  }
  * { margin: 0; padding: 0; box-sizing: border-box; }
  html, body {
    width: 1200px;
    height: 1200px;
    overflow: hidden;
    background: var(--backdrop);
  }
  .canvas {
    width: 1200px;
    height: 1200px;
    display: flex;
    flex-direction: column;
    align-items: center;
    justify-content: center;
    gap: 40px;
  }
  .card {
    position: relative;
    width: 960px;
    height: 548px;
    box-shadow: 0 14px 40px rgba(0,0,0,0.35);
    overflow: hidden;
  }
  .card--front { background: var(--card-front); }
  .card--back { background: var(--card-back); }

  .mark {
    position: absolute;
    border: 5px solid var(--gold);
    border-radius: 50%;
  }
  .card--front .mark {
    width: 200px; height: 200px;
    left: 440px; top: 70px;
  }
  .card--back .mark {
    width: 190px; height: 190px;
    left: 385px; top: 110px;
  }

  .title-row {
    position: absolute;
    left: 0; right: 0;
    top: 300px;
    display: flex;
    align-items: flex-start;
  }
  .rule {
    flex: 1;
    height: 3px;
  }
  .rule--gold { background: var(--gold); margin-top: 62px; }
  .rule--white { background: var(--white); margin-top: 54px; }
  .title {
    font-family: "Cinzel", serif;
    text-align: left;
    padding: 0 8px;
  }
  .title__name {
    color: var(--white);
    font-size: 44px;
    font-weight: 500;
    letter-spacing: 1px;
    line-height: 1;
  }
  .title__trade {
    color: var(--gold);
    font-size: 40px;
    letter-spacing: 2px;
    line-height: 1.1;
  }
  .contact {
    position: absolute;
    left: 0; right: 0;
    top: 420px;
    text-align: center;
    font-family: "Arimo", sans-serif;
    font-size: 21px;
    line-height: 1.35;
  }
  .contact__email { color: var(--white); }
  .contact__phone { color: var(--gold); }

  .back-name {
    position: absolute;
    left: 0; right: 0;
    top: 340px;
    text-align: center;
    font-family: "Cinzel", serif;
    font-size: 40px;
    font-weight: 500;
    color: var(--white);
    letter-spacing: 1px;
  }
</style>
</head>
<body>
<main class="canvas">
  <section class="card card--front">
    <div class="mark" aria-hidden="true"></div>
    <div class="title-row">
      <div class="rule rule--gold"></div>
      <h1 class="title">
        <span class="title__name">Dane Calloway</span><br>
        <span class="title__trade">Photography</span>
      </h1>
      <div class="rule rule--white"></div>
    </div>
    <div class="contact">
      <p class="contact__email">dane.calloway@lumenmail.com</p>
      <p class="contact__phone">+64155020488</p>
    </div>
  </section>

  <section class="card card--back">
    <div class="mark" aria-hidden="true"></div>
    <p class="back-name">Dane Calloway</p>
  </section>
</main>
</body>
</html>
```